Velmora Resident Safety and Security

Need a website for our company. Please see attached outlines and files
Main Page
Velmora
Design – Install – Maintain
Supporting the Safety and Security needs of your Community
Best in Class Systems for the Safety and Security of your Residents and Staff
Your Trusted Advisor
Solutions
Systems tailored to the needs of your facility
Skilled Nursing Facilities
Long Term Care
CCRC’s
Assisted Living
Independent Living
Access Control
Maglocks
Keypads
Prox readers (key fob, card, etc.)
Wireless locks
Multi-Tennant
Perimeter doors
Resident Apartment doors
Nurse Call
Tone / Visual
Fixed Stations
Dome Lights
T/V+ Audio
Fixed Stations
Dome Lights
Audio communication
Wireless
Fixed Stations
Resident Pendants
Hybrid Systems
Wired and Wireless integrated for seamless notification and reporting.
CCTV
Surveillance systems to fit your security needs and your budget
Remote Access, Local or Cloud Storage
Good, Better, Best proposals
Wander management
Door Alarming
Detection of wandering resident
Remote alarming and alerts
Delay elopement to allow for redirection
Network Infrastructure
Modern infrastructure for modern systems
Conference and Telepresence
Professionally installed systems to allow for seamless clear communications between teams across infinite distances.
Our Team
Rolf Amundsen – President
Patricia Lowell – Vice President of Customer Success
Miles Forbush – Account Executive
Industry Associations
Harborline Collective
Massachusetts chapter of the National Guild of Elder Care Stewards
Contact Us
Phone (603) 555-0172
Email Info@Velmora.example
Facilities we serve
Independent Senior Living
Assisted Living
Memory Care
CCRC (Continuing Care Retirement Community)
Skilled Nursing / Rehab
Multi-Tenant
Outpatient Surgical Centers
Endoscopy Clinics
Acute Care
Urgent Care
Commercial Properties of all types
General notes
Imagery should invoke high tech, safety, security and include healthcare themes. the circuit board shield is our logo and a ghosted image as back ground or some animation that brings in the logo or the circuit board should be incorporated.
Velmora is a systems integration company specializing in low voltage solutions for healthcare facilities and senior living communities. The company aims to leverage its industry expertise, and innovative products to become the market leader in systems integration, focusing on enhancing safety and operational efficiency.
Vision and Mission: Velmora’s vision is to revolutionize integrated systems within healthcare and commercial environments by delivering innovative, reliable, and tailored solutions that enhance operational efficiency and patient care. The company is committed to setting new standards for resident safety and customer satisfaction.
Company Summary: Founded by experienced industry professionals, Velmora specializes in the design, installation, and maintenance of systems including Access Control, Nurse Call, Delayed Egress, network infrastructure, and overhead paging primarily for healthcare clients.
Products and Services: The company offers a comprehensive range of low voltage systems including Nurse Call (wired and wireless), Wander Management, Access Control, and wired/wireless network infrastructure tailored for senior living and healthcare facilities.
Mission Statement
Velmora was founded to fill a specific need. Senor living communities and healthcare facilities of all kinds face unique challenges in regards to technology and systems integration. Velmora is perfectly positioned with an experienced management team, skilled technicians, industry relationships with suppliers and facility management groups. We have built our reputation on excellent customer service and the highest standards of integrity. Velmora’s vision is to revolutionize integrated systems within healthcare and commercial environments by delivering innovative, reliable, and tailored solutions that enhance operational efficiency and patient care. We are committed to setting new standards for resident safety and customer satisfaction in every project we undertake.

Target Market(s)

Senior living communities staff and management

Industry/Entity Type

Systems Intergration

Coding

Coded - Design and coding required

Font styles to use
Serif
Sans Serif

Colors
0054AA
0677BA
7BADD7
CADEEF
E8F1F8
0094D4
00A9DD
6FCCEA
C7EBF8
E9F6FB

Requirements
Must have
• unique eye catching design including circuit board (PCB) type design and our supplied logo files

```html
<!DOCTYPE html>
<html lang="en">
<head>
<meta charset="utf-8">
<title>Velmora Resident Safety and Security</title>
<link href="https://fonts.googleapis.com/css2?family=Inter:wght@400;500;600;700;800;900&display=swap" rel="stylesheet">
<style>
:root{
  --navy:#141b2d;
  --navy-2:#1d2436;
  --deep:#0054AA;
  --blue:#0677BA;
  --sky:#0094D4;
  --cyan:#00A9DD;
  --pale-cyan:#C7EBF8;
  --mist:#CADEEF;
  --ice:#E8F1F8;
  --ink:#1b2233;
  --text:#4a5263;
  --green:#22b35e;
  --light-bg:#f6f8fb;
}
*{box-sizing:border-box;margin:0;padding:0}
html,body{width:1200px;height:4434px;overflow:hidden}
body{position:relative;font-family:"Inter",Arial,sans-serif;color:var(--ink);background:#fff}
.abs{position:absolute}
.btn{position:absolute;display:flex;align-items:center;justify-content:center;border-radius:24px;font-weight:700;font-size:15px}
.btn-sky{background:var(--sky);color:#fff;box-shadow:0 4px 10px rgba(0,148,212,.3)}
.btn-white{background:#fff;color:var(--deep)}
.eyebrow{font-size:13px;font-weight:700;letter-spacing:1.6px;color:var(--sky);text-transform:uppercase}
.section-title{font-size:29px;font-weight:800;text-transform:uppercase;letter-spacing:-.2px}
.center{left:0;width:1200px;text-align:center}

/* nav */
.nav{top:0;left:0;width:1200px;height:76px;background:#fff}
.brand{display:flex;align-items:center;gap:8px;font-weight:800;color:var(--deep)}
.brand-dot{width:18px;height:18px;border-radius:50%;background:var(--sky)}
.nav .brand{position:absolute;left:52px;top:24px;font-size:20px}
.nav-links{position:absolute;left:372px;top:26px;display:flex;gap:30px;font-size:14px;font-weight:500;color:#333}

/* hero */
.hero-stripe{top:76px;left:0;width:1200px;height:730px;background:var(--sky);clip-path:polygon(0 0,100% 0,100% 615px,50% 730px,0 615px)}
.hero{top:76px;left:0;width:1200px;height:700px;background:linear-gradient(160deg,#0b1e44 0%,#0a3a7c 55%,#0b5cae 100%);clip-path:polygon(0 0,100% 0,100% 578px,50% 700px,0 578px)}
.hero-eyebrow{left:52px;top:206px;color:var(--cyan);font-size:13px}
.hero-title{left:52px;top:226px;font-size:58px;line-height:57px;font-weight:900;color:#fff;text-transform:uppercase;letter-spacing:-.5px}
.hero-title span{color:var(--cyan)}
.hero-copy{left:52px;top:480px;width:500px;font-size:16.5px;line-height:26px;color:#e2ecf8}
.hero-photo{left:600px;top:170px;width:546px;height:376px;border:4px solid #d7dee8;border-radius:6px;background:linear-gradient(135deg,#cfd6df 0%,#9aa5b3 45%,#3b3f46 100%);transform:rotate(1.6deg);box-shadow:0 20px 40px rgba(0,0,0,.35)}
.heart-badge{left:845px;top:153px;width:56px;height:56px;border-radius:50%;background:#fff;display:flex;align-items:center;justify-content:center;box-shadow:0 6px 16px rgba(0,0,0,.3)}
.emblem{left:502px;top:672px;width:196px;height:196px;display:flex;align-items:center;justify-content:center}
.emblem-diamond{position:absolute;left:30px;top:30px;width:136px;height:136px;background:#fff;border:5px solid var(--navy);outline:4px solid var(--sky);outline-offset:-12px;transform:rotate(45deg);border-radius:14px}
.emblem .brand{position:relative;flex-direction:column;gap:6px;font-size:16px;color:var(--blue)}

/* services */
.tagline{left:452px;top:878px;width:296px;text-align:center;font-size:13px;font-weight:700;letter-spacing:1.8px;color:var(--deep);border-bottom:2px solid var(--mist);padding-bottom:5px;background:#fff}
.card{position:absolute;top:990px;width:346px;height:345px;background:#fff;border-radius:8px;box-shadow:0 8px 24px rgba(20,40,80,.12);overflow:hidden}
.card-head{height:95px;display:flex;align-items:center;gap:14px;padding-left:22px;font-weight:700;font-size:15.5px;color:#fff}
.card-head .ico{width:44px;height:44px;border-radius:50%;background:#fff;display:flex;align-items:center;justify-content:center}
.card-img{margin:22px 24px 0;height:119px;border-radius:3px}
.card p{margin:22px 24px 0;font-size:13px;line-height:19px;color:var(--text)}

/* about */
.hex{clip-path:polygon(25% 0,75% 0,100% 50%,75% 100%,25% 100%,0 50%)}
.about-img{left:131px;top:1546px;width:360px;height:362px;background:radial-gradient(circle at 50% 50%,#6b6f72 0%,#9ba7a2 35%,#c7cfca 70%,#7e8884 100%)}
.about-title{left:630px;top:1582px;font-size:34px;line-height:38px;font-weight:800;text-transform:uppercase}
.about-copy{left:630px;width:510px;font-size:15px;line-height:25px;color:var(--text)}

/* why */
.why-shape{top:2070px;left:0;width:1200px;height:770px}
.why-hex{position:absolute;top:2335px;width:346px;height:300px;display:flex;flex-direction:column;align-items:center;justify-content:center;text-align:center;padding:0 56px}
.why-hex h3{font-size:17px;font-weight:700;margin:18px 0 10px}
.why-hex p{font-size:13px;line-height:20px;color:var(--text)}

/* table */
.matrix{left:52px;top:3027px;width:1096px;border-collapse:collapse;background:#fff;border-radius:8px;overflow:hidden;box-shadow:0 8px 24px rgba(20,40,80,.12)}
.matrix th{height:67px;font-size:15px;font-weight:700;color:#fff;text-align:center}
.matrix th:first-child{text-align:left;padding-left:22px;background:var(--navy);width:316px}
.matrix td{height:50px;border-top:1px solid #e8ecf2;text-align:center}
.matrix td:first-child{text-align:left;padding-left:15px;font-size:13px;font-weight:700;color:var(--ink)}
.matrix .med{background:#eef5fd}
.tick{display:inline-block;width:14px;height:14px;border-radius:50%;background:var(--green);vertical-align:middle}
.tick.off{background:#d7dbe0}

/* team */
.team-bg{top:3499px;left:0;width:1200px;height:700px;background:var(--light-bg)}
.member{position:absolute;top:3682px;width:346px;height:280px;background:#fff;border-radius:8px;box-shadow:0 8px 24px rgba(20,40,80,.12);overflow:hidden}
.member-top{position:relative;height:180px;background:linear-gradient(180deg,#0b1d3f 0%,#0a4d96 100%);border-top:4px solid var(--sky)}
.initials{position:absolute;right:40px;top:10px;font-size:120px;font-weight:400;color:rgba(215,220,228,.85);letter-spacing:-2px}
.member-name{position:absolute;left:15px;top:130px;color:#fff;font-size:17px;font-weight:700}
.member-role{position:absolute;left:15px;top:152px;color:var(--pale-cyan);font-size:11px;font-weight:700;text-transform:uppercase}
.member p{padding:22px 22px 0;font-size:11.5px;line-height:18px;color:var(--text)}

/* footer */
.footer-stripe{top:3975px;left:0;width:1200px;height:459px;background:var(--sky);clip-path:polygon(0 0,50% 155px,100% 0,100% 100%,0 100%)}
.footer{top:3995px;left:0;width:1200px;height:439px;background:var(--navy);clip-path:polygon(0 0,50% 150px,100% 0,100% 100%,0 100%)}
.fcol{position:absolute;top:4183px;font-size:13px;line-height:26px;color:#c3cad6}
.fcol h4{font-size:15px;font-weight:700;color:var(--sky);margin-bottom:8px}
.fcol .row{display:flex;align-items:center;gap:10px}
.social{display:flex;gap:16px;margin-top:12px}
.social span{width:28px;height:28px;border-radius:50%;background:#fff}
.copyright{top:4382px;font-size:11px;color:#7c8596}
</style>
</head>
<body>

<!-- navigation -->
<header class="abs nav">
  <div class="brand"><span class="brand-dot"></span>Velmora</div>
  <nav class="nav-links"><span>Home</span><span>About Us</span><span>Services</span><span>Team</span><span>Facilities</span></nav>
  <div class="btn btn-sky" style="left:997px;top:17px;width:151px;height:34px;font-size:13px">Request a Quote</div>
</header>

<!-- hero -->
<div class="abs hero-stripe"></div>
<section class="abs hero" style="top:76px"></section>
<div class="abs eyebrow hero-eyebrow">Design • Install • Maintain</div>
<h1 class="abs hero-title">Smart Systems<br>For<br><span>Safer<br>Communities</span></h1>
<p class="abs hero-copy">Automate your facility's safety. We are the single source for Nurse Call, Access Control, and Low-Voltage infrastructure.</p>
<div class="btn btn-sky" style="left:52px;top:561px;width:188px;height:45px">Explore Solutions</div>
<div class="btn btn-white" style="left:255px;top:561px;width:140px;height:45px">Contact Us</div>
<div class="abs hero-photo" role="img" aria-label="Doctor in a white coat holding a smartphone"></div>
<div class="abs heart-badge">
  <svg width="30" height="30" viewBox="0 0 24 24"><path d="M12 21s-8-5.3-8-11a4.5 4.5 0 0 1 8-2.8A4.5 4.5 0 0 1 20 10c0 5.7-8 11-8 11z" fill="var(--deep)"/><path d="M5 12h4l1.5-3 2 6 1.5-3h5" stroke="#fff" stroke-width="1.6" fill="none"/></svg>
</div>
<div class="abs emblem">
  <div class="emblem-diamond"></div>
  <div class="brand"><span class="brand-dot" style="width:30px;height:30px"></span>Velmora</div>
</div>

<!-- services -->
<div class="abs tagline">TRANSFORM THE WAY YOU CARE</div>
<h2 class="abs section-title center" style="top:918px">Optimise Your Systems</h2>

<article class="card" style="left:52px">
  <div class="card-head" style="background:var(--mist);color:var(--deep)"><span class="ico"><svg width="20" height="20" viewBox="0 0 24 24" fill="var(--deep)"><circle cx="12" cy="8" r="4"/><path d="M4 21c0-4.4 3.6-7 8-7s8 2.6 8 7z"/></svg></span>Nurse Call Systems</div>
  <div class="card-img" role="img" aria-label="Hospital patient room with medical equipment" style="background:linear-gradient(135deg,#8a8f91,#c9cdca 50%,#6d6f68)"></div>
  <p>Allow residents to call for help from their bed. High end systems allow direct communication to caregivers.</p>
</article>
<article class="card" style="left:427px">
  <div class="card-head" style="background:var(--blue)"><span class="ico"><svg width="20" height="20" viewBox="0 0 24 24" fill="var(--blue)"><circle cx="12" cy="7" r="4"/><rect x="6" y="13" width="12" height="8" rx="2"/></svg></span>Wander Management</div>
  <div class="card-img" role="img" aria-label="Caregiver assisting a senior resident" style="background:linear-gradient(135deg,#7b6a5a,#b49a8a 50%,#4e4238)"></div>
  <p>Secure transmitters and door controllers prevent eloping. Alarms sound instantly if residents enter reception fields.</p>
</article>
<article class="card" style="left:802px">
  <div class="card-head" style="background:var(--sky)"><span class="ico"><svg width="20" height="20" viewBox="0 0 24 24"><rect x="3" y="6" width="18" height="12" rx="2" fill="var(--sky)"/><circle cx="8.5" cy="12" r="2" fill="#fff"/><path d="M13 10.5h5M13 13.5h4" stroke="#fff" stroke-width="1.5"/></svg></span>Access Control</div>
  <div class="card-img" role="img" aria-label="Red padlock on a glowing green keyboard" style="background:linear-gradient(135deg,#1c2a1c,#9b1d1d 50%,#1f5f2a)"></div>
  <p>Control who enters a space and log events. Generate reports in the event of an incident.</p>
</article>
<div class="btn btn-sky" style="left:497px;top:1364px;width:206px;height:41px">Explore All Services</div>

<!-- about -->
<div class="abs hex" style="left:90px;top:1788px;width:110px;height:120px;background:var(--ice)"></div>
<div class="abs hex about-img" role="img" aria-label="Surgical team looking down under an operating lamp"></div>
<div class="abs hex" style="left:456px;top:1546px;width:76px;height:74px;background:#a9dbf0"></div>
<div class="abs eyebrow" style="left:630px;top:1555px;color:var(--blue);letter-spacing:.6px">About Velmora</div>
<h2 class="abs about-title">See Everything.<br>Act Instantly.</h2>
<p class="abs about-copy" style="top:1680px">Velmora was founded to fill a specific need. Senior living communities face unique challenges in regards to technology. We leverage industry expertise to become the market leader in systems integration.</p>
<p class="abs about-copy" style="top:1775px">Our vision is to revolutionize integrated systems within healthcare by delivering innovative, reliable, and tailored solutions that enhance operational efficiency.</p>
<div class="btn btn-sky" style="left:630px;top:1873px;width:171px;height:38px">Meet Our Team</div>

<!-- why choose -->
<svg class="abs why-shape" viewBox="0 0 1200 770" preserveAspectRatio="none" aria-hidden="true">
  <defs><linearGradient id="whyGrad" x1="0" y1="0" x2="1" y2="1"><stop offset="0" stop-color="#0054AA"/><stop offset="1" stop-color="#0094D4"/></linearGradient></defs>
  <polygon points="0,130 620,0 1200,120 1200,770 0,770" fill="var(--navy)"/>
  <polygon points="0,158 620,28 1200,148 1200,768 0,768" fill="url(#whyGrad)"/>
</svg>
<div class="abs eyebrow center" style="top:2210px;color:#dfeaf6;letter-spacing:.8px">Why Choose Velmora</div>
<h2 class="abs section-title center" style="top:2238px;color:#fff;font-size:31px">Infrastructure for Modern Facilities</h2>
<div class="why-hex hex" style="left:52px;background:#fff">
  <svg width="42" height="36" viewBox="0 0 24 22" fill="none" stroke="var(--sky)" stroke-width="2"><rect x="9" y="1" width="6" height="5"/><rect x="2" y="15" width="6" height="5"/><rect x="16" y="15" width="6" height="5"/><path d="M12 6v4M5 15v-5h14v5"/></svg>
  <h3>Wired &amp; Wireless</h3>
  <p>Network cable, switches, and wireless access points for every task.</p>
</div>
<div class="why-hex hex" style="left:412px;top:2321px;width:377px;height:331px;background:var(--navy);color:#fff">
  <svg width="40" height="36" viewBox="0 0 24 22" fill="var(--sky)"><path d="M2 8h5l10-6v18L7 14H2z"/><path d="M5 14l2 6h3l-2-6z"/></svg>
  <h3>Overhead Paging</h3>
  <p style="color:#b8c2d2">Efficiently make announcements. Integrated with business phones.</p>
</div>
<div class="why-hex hex" style="left:802px;background:#fff">
  <svg width="44" height="34" viewBox="0 0 24 18" fill="none" stroke="var(--sky)" stroke-width="2.2" stroke-linecap="round"><path d="M2 6a14 14 0 0 1 20 0M5.5 9.5a9 9 0 0 1 13 0M9 13a4 4 0 0 1 6 0"/><circle cx="12" cy="16" r="1.2" fill="var(--sky)"/></svg>
  <h3>Wireless Pendants</h3>
  <p>Locate residents instantly and provide location data to caregivers.</p>
</div>
<div class="btn btn-white" style="left:508px;top:2688px;width:184px;height:40px">Request A Quote</div>

<!-- expertise table -->
<div class="abs eyebrow center" style="top:2931px">Our Expertise</div>
<h2 class="abs section-title center" style="top:2948px">Proven Performance Across Industries</h2>
<table class="abs matrix">
  <thead><tr><th>Solutions</th><th style="background:var(--blue);width:255px">Senior Living</th><th style="background:var(--sky);width:284px">Medical / Acute</th><th style="background:var(--navy-2)">Commercial</th></tr></thead>
  <tbody>
    <tr><td>Nurse Call Integration</td><td><span class="tick"></span></td><td class="med"><span class="tick"></span></td><td><span class="tick off"></span></td></tr>
    <tr><td>Wander Management</td><td><span class="tick"></span></td><td class="med"><span class="tick"></span></td><td><span class="tick off"></span></td></tr>
    <tr><td>Access Control</td><td><span class="tick"></span></td><td class="med"><span class="tick"></span></td><td><span class="tick"></span></td></tr>
    <tr><td>Overhead Paging</td><td><span class="tick"></span></td><td class="med"><span class="tick"></span></td><td><span class="tick"></span></td></tr>
    <tr><td>Network Infrastructure</td><td><span class="tick"></span></td><td class="med"><span class="tick"></span></td><td><span class="tick"></span></td></tr>
  </tbody>
</table>
<div class="btn btn-sky" style="left:510px;top:3383px;width:180px;height:32px;font-size:13px">View Full Facility List</div>

<!-- team -->
<div class="abs team-bg"></div>
<div class="abs eyebrow center" style="top:3576px;color:var(--blue)">Our People</div>
<h2 class="abs section-title center" style="top:3601px">Purpose-Built for High Performance</h2>
<article class="member" style="left:52px">
  <div class="member-top"><span class="initials">RA</span><div class="member-name">Rolf Amundsen</div><div class="member-role">President</div></div>
  <p>20 year veteran of the telecommunications industry. Rolf brings the technical and business acumen to lead Velmora to success.</p>
</article>
<article class="member" style="left:427px">
  <div class="member-top"><span class="initials">PL</span><div class="member-name">Patricia Lowell</div><div class="member-role">VP Customer Success</div></div>
  <p>With over 20 years leading service departments, Patricia brings in-depth knowledge of client systems and challenges.</p>
</article>
<article class="member" style="left:802px">
  <div class="member-top"><span class="initials">MF</span><div class="member-name">Miles Forbush</div><div class="member-role">Account Executive</div></div>
  <p>Dedicated to ensuring every facility receives the tailored solutions they need for safety and efficiency.</p>
</article>

<!-- footer -->
<div class="abs footer-stripe"></div>
<footer class="abs footer"></footer>
<div class="fcol" style="left:52px;width:240px">
  <div class="brand" style="color:var(--sky);font-size:18px;margin-bottom:14px"><span class="brand-dot"></span>Velmora</div>
  <p style="line-height:19px">Revolutionizing integrated systems within healthcare and commercial environments.</p>
</div>
<div class="fcol" style="left:334px"><h4>Quick Links</h4><div>Home</div><div>About Us</div><div>Services</div></div>
<div class="fcol" style="left:615px"><h4>Contact Info</h4>
  <div class="row"><svg width="12" height="14" viewBox="0 0 24 28" fill="#c3cad6"><path d="M12 0a10 10 0 0 0-10 10c0 7.5 10 18 10 18s10-10.5 10-18A10 10 0 0 0 12 0zm0 14a4 4 0 1 1 0-8 4 4 0 0 1 0 8z"/></svg>New England Region</div>
  <div class="row"><svg width="13" height="13" viewBox="0 0 24 24" fill="#c3cad6"><path d="M6.6 10.8a15 15 0 0 0 6.6 6.6l2.2-2.2a1 1 0 0 1 1-.25 11.4 11.4 0 0 0 3.6.6 1 1 0 0 1 1 1V20a1 1 0 0 1-1 1A17 17 0 0 1 3 4a1 1 0 0 1 1-1h3.5a1 1 0 0 1 1 1c0 1.25.2 2.45.6 3.6a1 1 0 0 1-.25 1z"/></svg>(603) 555-0172</div>
  <div class="row"><svg width="13" height="11" viewBox="0 0 24 18" fill="#c3cad6"><path d="M0 0h24v18H0z"/><path d="M0 1l12 8 12-8" stroke="var(--navy)" stroke-width="2" fill="none"/></svg>Info@Velmora.example</div>
</div>
<div class="fcol" style="left:895px"><h4>Associations</h4><div>Harborline Collective</div><div>NGECS (MA Chapter)</div>
  <div class="social"><span role="img" aria-label="Professional network profile"></span><span role="img" aria-label="Social media page"></span></div>
</div>
<div class="abs copyright center">© 2025 Velmora. All Rights Reserved.</div>

</body>
</html>
```